Limousine Service Company Website

we need a website designed for a national limousine company with global capabilities (meaning they can service clients throughout the US and the world)

They service mostly corporate/business travelers, and groups and meetings, with a small portion of their business devoted to retail clients (special events and personal travel)

The overall look should be corporate, and we prefer a responsive design. We will need a home page, a fleet page (examples can be seen here: https://www.brovalecars.com/fleet
http://www.pennowayrides.com/our-fleet) and one interior page

Copy will be lorem epsum for now

We have no logo yet but can put a placeholder logo

```html
<!DOCTYPE html>
<html lang="en">
<head>
<meta charset="utf-8">
<title>Crestline Limousine</title>
<link rel="stylesheet" href="https://fonts.googleapis.com/css2?family=Varela+Round&family=Open+Sans:wght@400;600&display=swap">
<style>
:root{
  --ink:#1e1e1e;
  --text:#555;
  --muted:#777;
  --gold:#c99a3b;
  --ring:#e2e2e2;
  --blue:#2d6fb8;
  --blue-dark:#1b4f8e;
  --nav-top:#fdfdfd;
  --nav-bottom:#e9e9e9;
  --nav-line:#dcdcdc;
  --footer:#262626;
  --white:#fff;
  --panel:#f1f1f1;
}
*{margin:0;padding:0;box-sizing:border-box}
html,body{width:759px;height:1200px;overflow:hidden;background:var(--white)}
body{position:relative;font-family:"Open Sans",Arial,sans-serif;color:var(--text)}
.abs{position:absolute}

/* header */
.brand{left:54px;top:20px;display:flex;align-items:center;gap:10px}
.brand-ring{width:78px;height:78px;border:1px solid var(--ink);border-radius:50%}
.brand-name{font-family:"Varela Round",sans-serif;font-size:21px;line-height:1.05;color:var(--ink);width:120px}
.phone{right:56px;top:35px;font-family:"Varela Round",sans-serif;font-size:15px;color:var(--ink);display:flex;align-items:center;gap:8px}
.reserve{left:530px;top:69px;width:172px;height:45px;border-radius:22px;background:linear-gradient(#4b94dc,var(--blue) 55%,var(--blue-dark));color:var(--white);text-align:center;padding-top:7px;box-shadow:0 2px 3px rgba(0,0,0,.25)}
.reserve strong{display:block;font-family:"Varela Round",sans-serif;font-weight:400;font-size:14px;line-height:16px}
.reserve span{display:block;font-size:8px;line-height:12px}

/* nav */
.nav{left:0;top:129px;width:759px;height:37px;background:linear-gradient(var(--nav-top),var(--nav-bottom));display:flex;padding-left:54px}
.nav a{font-size:10.5px;color:#333;text-decoration:none;line-height:37px;padding:0 17px;border-right:1px solid var(--nav-line)}
.nav a.active{background:var(--gold);color:var(--white);padding:0 18px}

/* hero */
.hero{left:0;top:166px;width:759px;height:291px;background:linear-gradient(100deg,#6a6a6a,#b8b8b8 45%,#ececec 80%,#d6d6d6)}
.fleet-shot{left:148px;top:330px;width:556px;height:165px;border-radius:30px 30px 10px 10px;background:linear-gradient(#3a3a3a,#151515)}
.slide-btn{top:425px;width:18px;height:18px;background:#7a7a7a;display:flex;align-items:center;justify-content:center}

/* services */
.section-title{font-family:"Varela Round",sans-serif;font-size:20px;color:var(--ink)}
.services-title{left:0;width:759px;top:518px;text-align:center}
.intro{left:56px;width:647px;top:556px;font-size:8.6px;line-height:16px;text-align:center}
.service{top:615px;width:200px;text-align:center}
.service svg{display:block;margin:0 auto}
.service h3{font-family:"Varela Round",sans-serif;font-weight:400;font-size:14px;color:var(--gold);margin-top:8px}
.service p{font-size:8.6px;line-height:16px;margin-top:6px}
.divider{left:90px;top:800px;width:580px;height:14px;background:radial-gradient(ellipse at top,rgba(0,0,0,.09),transparent 70%)}

/* welcome */
.welcome-title{left:56px;top:844px;font-size:18px}
.welcome-copy{left:54px;top:881px;width:392px;font-size:8.6px;line-height:16px}
.welcome-copy p+p{margin-top:3px}

/* newsletter */
.newsletter{left:490px;top:848px;width:212px;height:164px;background:var(--panel);border:1px solid #e4e4e4}
.newsletter h4{height:31px;background:linear-gradient(#3e86d0,var(--blue-dark));color:var(--white);font-family:"Varela Round",sans-serif;font-weight:400;font-size:14px;line-height:31px;padding-left:12px}
.field{margin:14px 10px 0;height:27px;background:var(--white);border:1px solid #d6d6d6;font-size:8.6px;line-height:25px;padding-left:10px;color:#666}
.field+.field{margin-top:12px}
.submit{position:absolute;right:10px;bottom:12px;width:52px;height:23px;background:linear-gradient(#555,#2a2a2a);color:var(--white);font-size:10px;font-weight:600;text-align:center;line-height:23px;border-radius:2px}

/* footer */
.footer{left:0;top:1038px;width:759px;height:162px;background:var(--footer);color:var(--white);text-align:center}
.socials{display:flex;justify-content:center;gap:10px;margin-top:30px}
.socials span{width:38px;height:38px;border:1.5px solid #e6e6e6;border-radius:50%}
.footer-links{margin-top:16px;font-size:9px}
.footer-links a{color:var(--white);text-decoration:none;padding:0 4px}
.copyright{margin-top:9px;font-size:8.6px}
</style>
</head>
<body>

<header>
  <div class="abs brand">
    <span class="brand-ring"></span>
    <span class="brand-name">Crestline Limousine</span>
  </div>
  <div class="abs phone">+61 02 5550 1742
    <svg width="12" height="14" viewBox="0 0 12 14"><path d="M2 1l3 0 1 3-2 1.5c.8 2 2 3.3 3.8 4.2L9.5 8l2.5 1.2v3L10.5 13C5 12 1 7 1 2z" fill="#555"/></svg>
  </div>
  <div class="abs reserve"><strong>Make a Reservation</strong><span>Submit a reservation request</span></div>
</header>

<nav class="abs nav">
  <a class="active" href="#">HOME</a><a href="#">ABOUT</a><a href="#">SERVICES</a><a href="#">OUR FLEET</a><a href="#">TOURS</a><a href="#">MEETINGS &amp; EVENTS</a><a href="#">BLOG</a><a href="#">CONTACT</a>
</nav>

<div class="abs hero" role="img" aria-label="Blurred black-and-white modern building facade behind the fleet"></div>
<div class="abs fleet-shot" role="img" aria-label="Black luxury sedan beside a black passenger van"></div>
<div class="abs slide-btn" style="left:57px"><svg width="6" height="9"><path d="M5 1L1.5 4.5 5 8" stroke="#fff" fill="none" stroke-width="1.4"/></svg></div>
<div class="abs slide-btn" style="left:80px"><svg width="6" height="9"><path d="M1 1l3.5 3.5L1 8" stroke="#fff" fill="none" stroke-width="1.4"/></svg></div>

<section>
  <h2 class="abs section-title services-title">Our Services</h2>
  <p class="abs intro">Typi non habent claritatem insitam; est usus legentis in iis qui facit eorum claritatem. Investigationes demonstraverunt lectores legere me lquod ii unt saepius. Clarit as est etiam processus dynamicus, qui sequitur mutationem consuetudium lectorum. Mirum est notare quam littecthic.</p>

  <div class="abs service" style="left:38px">
    <svg width="80" height="80" viewBox="0 0 80 80"><circle cx="40" cy="40" r="37" fill="none" stroke="var(--ring)" stroke-width="4"/><path d="M3 40A37 37 0 0 1 77 40" fill="none" stroke="var(--gold)" stroke-width="4"/><circle cx="40" cy="40" r="5" fill="none" stroke="#666" stroke-width="1.6"/><circle cx="40" cy="40" r="11" fill="none" stroke="#666" stroke-width="1.6" stroke-dasharray="5 3"/></svg>
    <h3>Corporate Travelers</h3>
    <p>Claritas est eteus dynamicuinquiqu conetlaritasdynamicusClaritas est nihil imp fiant sollemnes feiat lla.</p>
  </div>
  <div class="abs service" style="left:276px">
    <svg width="80" height="80" viewBox="0 0 80 80"><circle cx="40" cy="40" r="37" fill="none" stroke="var(--ring)" stroke-width="4"/><path d="M3 40A37 37 0 0 1 77 40" fill="none" stroke="var(--gold)" stroke-width="4"/><g fill="#666"><circle cx="40" cy="34" r="5"/><path d="M31 50c0-7 18-7 18 0z"/><circle cx="28" cy="37" r="4"/><path d="M21 50c0-6 12-6 12-2v2z"/><circle cx="52" cy="37" r="4"/><path d="M59 50c0-6-12-6-12-2v2z"/></g></svg>
    <h3>Groups and Meetings</h3>
    <p>Claritas est eteus dynamicuinquiqu conetlaritasdynamicusClaritas est nihil imp fiant sollemnes feiat lla.</p>
  </div>
  <div class="abs service" style="left:520px">
    <svg width="80" height="80" viewBox="0 0 80 80"><circle cx="40" cy="40" r="37" fill="none" stroke="var(--ring)" stroke-width="4"/><path d="M3 40A37 37 0 0 1 77 40" fill="none" stroke="var(--gold)" stroke-width="4"/><path d="M20 46v-8l6-6h22l8 7v7z" fill="none" stroke="#666" stroke-width="1.6"/><circle cx="29" cy="47" r="3.5" fill="#fff" stroke="#666" stroke-width="1.6"/><circle cx="49" cy="47" r="3.5" fill="#fff" stroke="#666" stroke-width="1.6"/></svg>
    <h3>Personal Travel</h3>
    <p>Claritas est eteus dynamicuinquiqu conetlaritasdynamicusClaritas est nihil imp fiant sollemnes feiat lla.</p>
  </div>
  <div class="abs divider"></div>
</section>

<section>
  <h2 class="abs section-title welcome-title">Welcome to Crestline Limousine</h2>
  <div class="abs welcome-copy">
    <p>Claritas est etiam processus dynamicus, qui sequitur mutationem consuetudium lectorum. Mirum est notare quam littera gothica, quam nunc putamus parum claram, anteposuerit litterarum formas humanitatis per seacula quarta decima et quinta decima. Eodem modo typi, qui nunc.</p>
    <p>Duis autem vel eum iriure dolor in hendrerit in vulputate velit esse molestie consequat, vel illum do lore eu feugiat nulla facilisis at vero eros et accumsan et iusto odio dignissim qui blandit praesent lu ptatum zzril delenit augue duis dolore te feugait nulla facilisi. Nam liber tempor cum soluta nobis el eifend option congue nihilimperdiet doming id quod mazim placerat face possim assum.</p>
  </div>
  <form class="abs newsletter">
    <h4>Newsletter Signup</h4>
    <div class="field">Name</div>
    <div class="field">Email</div>
    <div class="submit">SUBMIT</div>
  </form>
</section>

<footer class="abs footer">
  <div class="socials"><span></span><span></span><span></span><span></span></div>
  <div class="footer-links"><a href="#">Home</a>|<a href="#">Company</a>|<a href="#">Technology</a>|<a href="#">Applications</a>|<a href="#">Products</a>|<a href="#">Media Centre</a>|<a href="#">Career</a>|<a href="#">Contact</a></div>
  <p class="copyright">Copyright © 2013. All Rights Reserved.</p>
</footer>

</body>
</html>
```